New business card for my lawn and landscape business

Dorrin Yard and Building is a full-service lawn care, landscaping, and light construction company serving Paragould and the Northeast Arkansas region. The business is owned and operated by Marcus Toller, with a reputation for hands-on, detail-oriented service, dependable crews, and quality results for both residential and commercial clients. A well regarded business with great reviews.
Owner Marcus Toller
Dorrinyardandbuilding.example

Target Market(s)

Commercial, Middle, and upper class in north east Arkansas

Industry/Entity Type

Lawn maintenance and landscape

Contact Information for Business Card

Dorrin Yard And Building Professional lawn care, landscaping, and property improvement in Northeast Arkansas. • lawn maintenance •lawn treatments and weed control • exterior projects • Custom landscape design & installation • Sod, trees, rock & drainage solutions • Residential & commercial services Reliable. Detailed. Done right.

Requirements
Must have
• Business name, service area, list of some of our services, clean design that represents
Nice to have
• Unique. Different design element than just grass because its already in n the logo. Picture of a warm season (south) lawn or landscape. Pictures of the type of work we do

```html
<!DOCTYPE html>
<html lang="en">
<head>
<meta charset="utf-8">
<title>Dorrin Yard and Building – Business Card</title>
<link href="https://fonts.googleapis.com/css2?family=Heebo:ital,wght@0,400;0,500;0,600&display=swap" rel="stylesheet">
<style>
  :root {
    --stage: #000000;
    --paper: #ffffff;
    --ink: #111111;
    --leaf: #7cb53f;
    --leaf-bright: #8dc63f;
    --forest: #0b4528;
    --emerald: #00a651;
    --citron: #d7e31d;
    --bullet: #4cb648;
  }
  * { box-sizing: border-box; margin: 0; padding: 0; }
  html, body { width: 1200px; height: 1200px; overflow: hidden; background: var(--stage); }
  body { font-family: "Heebo", Arial, sans-serif; color: var(--ink); position: relative; }

  .card {
    position: absolute;
    left: 150px;
    width: 900px;
    height: 515px;
    border-radius: 22px;
    overflow: hidden;
  }

  /* Front */
  .card-front {
    top: 56px;
    background:
      radial-gradient(ellipse 55% 60% at 0% 100%, var(--citron) 0%, rgba(215,227,29,0) 100%),
      radial-gradient(ellipse 45% 50% at 85% 85%, var(--emerald) 0%, rgba(0,166,81,0) 100%),
      linear-gradient(180deg, rgba(11,69,40,0) 0%, rgba(11,69,40,0) 45%, rgba(0,150,70,0.85) 100%),
      linear-gradient(90deg, var(--leaf-bright) 0%, var(--leaf-bright) 38%, var(--forest) 60%, var(--forest) 100%);
  }
  .front-mark {
    position: absolute;
    left: 50%; top: 50%;
    transform: translate(-50%, -50%);
    display: flex; align-items: center; gap: 18px;
  }
  .front-mark .dot {
    width: 64px; height: 64px; border-radius: 50%; background: var(--ink);
  }
  .front-mark .name {
    font-weight: 600; font-size: 58px; letter-spacing: 4px; color: var(--ink);
  }

  /* Back */
  .card-back {
    top: 627px;
    background: var(--paper);
  }
  .back-mark {
    position: absolute; left: 48px; top: 58px;
    display: flex; align-items: center; gap: 10px;
  }
  .back-mark .dot { width: 34px; height: 34px; border-radius: 50%; background: var(--leaf); }
  .back-mark .name { font-weight: 600; font-size: 28px; letter-spacing: 2px; color: var(--leaf); }

  .services {
    position: absolute; left: 42px; top: 176px;
    list-style: none;
  }
  .services li {
    display: flex; align-items: center; gap: 7px;
    font-size: 18.5px; line-height: 26px; font-weight: 500;
  }
  .services li::before {
    content: ""; width: 16px; height: 16px; border-radius: 50%; background: var(--bullet); flex: none;
  }

  .owner { position: absolute; left: 670px; top: 192px; }
  .owner .person { font-size: 25px; font-weight: 500; line-height: 30px; }
  .owner .role { font-size: 21px; font-weight: 500; color: var(--leaf); line-height: 26px; }

  .website {
    position: absolute; left: 532px; top: 290px;
    display: flex; align-items: center; gap: 8px;
    font-size: 18.5px; font-weight: 500;
  }
  .website svg { width: 20px; height: 20px; }

  .edge-tab {
    position: absolute; right: -24px; top: 212px;
    width: 48px; height: 92px; border-radius: 50%; background: var(--leaf);
  }
  .base-band {
    position: absolute; right: 0; bottom: 0; width: 289px; height: 18px; background: var(--leaf);
  }

  .tagline { position: absolute; left: 41px; top: 420px; font-size: 15.5px; line-height: 21px; }
  .tagline .lead { color: var(--leaf); font-style: italic; }
</style>
</head>
<body>

<section class="card card-front" aria-label="Card front">
  <div class="front-mark">
    <span class="dot"></span>
    <span class="name">DORRIN</span>
  </div>
</section>

<section class="card card-back" aria-label="Card back">
  <div class="back-mark">
    <span class="dot"></span>
    <span class="name">DORRIN</span>
  </div>

  <ul class="services">
    <li>lawn maintenance</li>
    <li>lawn treatments and weed control</li>
    <li>exterior projects</li>
    <li>Custom landscape design &amp; installation</li>
    <li>Sod, trees, rock &amp; drainage solutions</li>
    <li>Residential &amp; commercial services Reliable</li>
  </ul>

  <div class="owner">
    <p class="person">Marcus Toller</p>
    <p class="role">Owner</p>
  </div>

  <div class="website">
    <span>Dorrinyardandbuilding.example</span>
    <svg viewBox="0 0 20 20" aria-hidden="true">
      <circle cx="10" cy="10" r="8.5" fill="none" stroke="var(--bullet)" stroke-width="2"/>
      <ellipse cx="10" cy="10" rx="3.5" ry="8.5" fill="none" stroke="var(--bullet)" stroke-width="1.6"/>
      <line x1="1.5" y1="10" x2="18.5" y2="10" stroke="var(--bullet)" stroke-width="1.6"/>
    </svg>
  </div>

  <span class="edge-tab"></span>
  <span class="base-band"></span>

  <div class="tagline">
    <p class="lead">Dorrin Yard And Building Professional lawn care</p>
    <p>Landscaping, and property improvement.</p>
    <p>Northeast Arkansas.</p>
  </div>
</section>

</body>
</html>
```